Business card design for a engineering company

I need a double sided business card design for my company "Verdmont Flow Solutions". The card will be used in Malaysia. Sleek and professional, with a little design flare to it.
Information to showcase:
1. Company logo
2. Name, title, phone, email address, website address
3. our products "Pumping technology, Valve & actuation, Air Moving Technology
Example:
Ravi Tanaka
Business manager
ravi.tanaka@verdmont-example.com
www.verdmont-example.com.my
- Pumping technology
- Valve & actuation
- Air moving technology
Target Market(s)
engineers, purchasing managers
Industry/Entity Type
Business
Contact Information for Business Card
Ravi Tanaka
Business manager
ravi.tanaka@verdmont-example.com
www.verdmont-example.com.my
- Pumping technology
- Valve & actuation
- Air moving technology
catch phrase : "Solving flow challenges, exceeding expectations"

```html
<!DOCTYPE html>
<html lang="en">
<head>
<meta charset="utf-8">
<title>Verdmont Flow Solutions – Business Card</title>
<link href="https://fonts.googleapis.com/css2?family=Open+Sans:wght@400;600;700&display=swap" rel="stylesheet">
<style>
  :root {
    --navy: #1f3a4a;
    --orange: #f7941d;
    --amber: #fbb034;
    --ink: #1c1c1c;
    --paper: #ffffff;
    --backdrop: #e9e6e1;
  }
  html, body {
    margin: 0;
    width: 1200px;
    height: 900px;
    overflow: hidden;
    background: var(--backdrop);
    font-family: "Open Sans", Arial, sans-serif;
  }
  .canvas { position: relative; width: 1200px; height: 900px; }
  .card {
    position: absolute;
    left: 320px;
    width: 560px;
    height: 320px;
    background: var(--paper);
    box-shadow: 0 6px 18px rgba(0,0,0,.15);
    overflow: hidden;
  }
  .card--front { top: 100px; }
  .card--back { top: 470px; }

  .brand {
    display: flex;
    align-items: center;
    gap: 12px;
    position: absolute;
  }
  .brand__mark {
    flex: none;
    width: 34px; height: 34px;
    background: var(--navy);
  }
  .brand__name {
    color: var(--navy);
    font-weight: 700;
    font-size: 26px;
    letter-spacing: 2px;
    line-height: 1.05;
    text-transform: uppercase;
    white-space: nowrap;
  }
  .card--front .brand { left: 0; right: 0; top: 104px; justify-content: center; }
  .tagline {
    position: absolute;
    left: 0; right: 0; top: 200px;
    margin: 0;
    text-align: center;
    font-size: 14px;
    color: var(--ink);
    text-transform: uppercase;
    letter-spacing: .3px;
  }

  .corner-accent { position: absolute; left: 0; top: 20px; }
  .holder { position: absolute; left: 62px; top: 22px; }
  .holder__name { font-weight: 700; font-size: 17px; color: var(--navy); margin: 0; }
  .holder__title { font-size: 12px; color: var(--ink); margin: 0; }

  .card--back .brand { left: 300px; top: 98px; gap: 10px; }
  .card--back .brand__mark { width: 32px; height: 32px; }
  .card--back .brand__name { font-size: 18px; letter-spacing: 1.5px; }

  .contacts {
    position: absolute; left: 28px; top: 146px;
    margin: 0; padding: 0; list-style: none;
    font-size: 12.5px; color: var(--ink);
  }
  .contacts li { display: flex; align-items: center; gap: 8px; height: 19px; white-space: nowrap; }
  .contacts svg { width: 11px; height: 11px; fill: var(--navy); }
  .products {
    position: absolute; left: 28px; top: 208px;
    font-size: 13.5px; color: var(--orange); margin: 0;
    white-space: nowrap;
  }
  .bands { position: absolute; left: 0; top: 0; }
</style>
</head>
<body>
<div class="canvas">

  <section class="card card--front" aria-label="Card front">
    <div class="brand">
      <span class="brand__mark"></span>
      <span class="brand__name">Verdmont Flow Solutions</span>
    </div>
    <p class="tagline">Solving flow challenges, exceeding expectations</p>
  </section>

  <section class="card card--back" aria-label="Card back">
    <svg class="corner-accent" width="44" height="34" viewBox="0 0 44 34">
      <polygon points="0,0 26,0 0,30" fill="var(--navy)"/>
      <polygon points="30,0 44,0 44,34 4,34" fill="var(--orange)"/>
    </svg>
    <div class="holder">
      <p class="holder__name">Ravi Tanaka</p>
      <p class="holder__title">Business manager</p>
    </div>

    <div class="brand">
      <span class="brand__mark"></span>
      <span class="brand__name">Verdmont<br>Flow Solutions</span>
    </div>

    <ul class="contacts">
      <li><svg viewBox="0 0 16 16"><path d="M3 1l3 3-2 2c1 2 3 4 5 5l2-2 3 3-2 3C6 15 1 10 0 3z"/></svg>10203040</li>
      <li><svg viewBox="0 0 16 16"><path d="M0 3h16v10H0zM1 4l7 5 7-5"/></svg>ravi.tanaka@verdmont-example.com</li>
      <li><svg viewBox="0 0 16 16"><circle cx="8" cy="8" r="8"/></svg>www.verdmont-example.com.my</li>
    </ul>
    <p class="products">Pumping Technology | Valve &amp; Actuation | Air Moving Technology</p>

    <svg class="bands" width="560" height="320" viewBox="0 0 560 320">
      <defs>
        <linearGradient id="band-orange" x1="0" y1="0" x2="1" y2="1">
          <stop offset="0" stop-color="var(--orange)"/>
          <stop offset="1" stop-color="var(--amber)"/>
        </linearGradient>
      </defs>
      <polygon points="0,240 198,240 184,262 0,262" fill="var(--navy)"/>
      <polygon points="204,266 560,266 560,304 180,304" fill="url(#band-orange)"/>
    </svg>
  </section>

</div>
</body>
</html>
```